KT Crewing business card

Require business card which includes:
Company name: KT CREWING PTY LTD
Email: Mick@ktcrewing.com.au
Phone: 0431 556 208
ACN: 517 238 649

slogan: Onsite Auto Electrician Labour hire

Details and logo on top side
Logo only on bottom side

colour codes : #F15A29 , #939598

Target Market(s)

Western Australia mining sector

Industry/Entity Type

Mining

Contact Information for Business Card

Require business card which includes: Company name: KT CREWING PTY LTD Email: Mick@ktcrewing.com.au Phone: 0431 556 208 ACN: 517 238 649 slogan: Onsite Auto Electrician Labour hire Details and logo on top side Logo only on bottom side colour codes : #F15A29 , #939598

Colors
EE7325
F08F49
F5BC92
FAE3D3
FDF4ED

Requirements
Must have
• double sided

```html
<!DOCTYPE html>
<html lang="en">
<head>
<meta charset="utf-8">
<title>KT Crewing – Business Card</title>
<link href="https://fonts.googleapis.com/css2?family=Montserrat:wght@500;600;700&display=swap" rel="stylesheet">
<style>
  :root {
    --backdrop: #d9d9d9;
    --navy: #303342;
    --orange: #f15a29;
    --white: #ffffff;
    --ink: #303342;
  }
  * { box-sizing: border-box; margin: 0; padding: 0; }
  html, body {
    width: 1200px; height: 1200px; overflow: hidden;
    background: var(--backdrop);
    font-family: "Montserrat", Arial, sans-serif;
  }
  .card {
    position: absolute;
    left: 237px;
    width: 726px;
    height: 414px;
    border-radius: 37px;
    overflow: hidden;
  }
  .card--front { top: 147px; background: var(--white); }
  .card--back  { top: 607px; background: var(--navy); }

  .front__brand-panel {
    position: absolute; left: 0; top: 0;
    width: 334px; height: 100%;
    background: var(--navy);
  }
  .front__stripe {
    position: absolute; left: 334px; top: 0;
    width: 11px; height: 100%;
    background: var(--orange);
  }
  .front__tab {
    position: absolute; left: 340px; top: 48px;
    width: 21px; height: 320px;
    background: var(--orange);
    border-radius: 0 14px 14px 0;
  }
  .brand {
    position: absolute; left: 0; width: 334px;
    text-align: center;
  }
  .brand__name {
    color: var(--orange);
    font-weight: 700;
    letter-spacing: 0.5px;
  }
  .front .brand__name { top: 170px; font-size: 34px; }
  .front .brand { top: 170px; }
  .brand__slogan {
    margin-top: 20px;
    color: var(--white);
    font-size: 9.5px;
    font-weight: 500;
    letter-spacing: 0.2px;
    text-transform: uppercase;
  }

  .company {
    position: absolute; left: 401px; top: 98px;
    color: var(--orange);
    font-size: 27px; font-weight: 700;
    letter-spacing: 0.2px;
    white-space: nowrap;
  }
  .contact {
    position: absolute; left: 409px; top: 208px;
    list-style: none;
    color: var(--ink);
    font-size: 14px; font-weight: 500;
  }
  .contact__row {
    display: grid;
    grid-template-columns: 63px auto;
    height: 39px;
    align-items: center;
  }

  .back .brand {
    left: 0; width: 100%; top: 170px;
  }
  .back .brand__name { font-size: 64px; letter-spacing: 1px; }
</style>
</head>
<body>
  <section class="card card--front front" aria-label="Business card front">
    <div class="front__brand-panel">
      <div class="brand">
        <p class="brand__name">KT Crewing</p>
        <p class="brand__slogan">Onsite Auto Electrician Labour Hire</p>
      </div>
    </div>
    <div class="front__stripe"></div>
    <div class="front__tab"></div>
    <h1 class="company">KT CREWING PTY LTD</h1>
    <ul class="contact">
      <li class="contact__row"><span>Phone :</span><span>0431 556 208</span></li>
      <li class="contact__row"><span>Email&nbsp; :</span><span>Mick@ktcrewing.com.au</span></li>
      <li class="contact__row"><span>ACN&nbsp;&nbsp;&nbsp; :</span><span>517 238 649</span></li>
    </ul>
  </section>

  <section class="card card--back back" aria-label="Business card back">
    <div class="brand">
      <p class="brand__name">KT Crewing</p>
    </div>
  </section>
</body>
</html>
```